Design and Renovation Company Luxury Business Card

I want to create a luxury business card for a Design and Renovation Firm . We will use our current logo. The company name is 742BUILD. We do not want anything standard. We need a very unique concept.
Please see uploaded inspiration. I really like the textured paper option. I would like the card to be thick with debossing, and/or embossing options. The logo has orange in it but I would like to see the card with and without the orange. I think the orange may make the company feel less high-end. The goal is to elevate the logo not match its vibe per se of the logo. We want something very unique, not standard at all!
I would like a space for :
Logo,
Name,
Position,
Email,
Office number,
Website Address,
Business Address,
Thank you!
Have fun!
Target Market(s)
Home owners Age 35 +
Industry/Entity Type
Design and Renovation
Contact Information for Business Card
Logo, Name, Position, Email, Office number, Website Address, Business Address,.
Colors
Designer to choose colors to be used in the design.
Requirements
Must have
- A luxury designer feel. Must be black or dark grey but open to other luxury ideas.
Nice to have
- Gold, silver, black embossing or debossing. Textured paper design.
Should not have
- A cheap look and feel.

```html
<!DOCTYPE html>
<html lang="en">
<head>
<meta charset="UTF-8">
<title>742BUILD Business Card</title>
<link rel="stylesheet" href="https://fonts.googleapis.com/css2?family=Montserrat:wght@500;700&family=Lato:wght@400&display=swap">
<style>
  :root {
    --backdrop: #e1e1e1;
    --crimson-core: #9c1a31;
    --crimson-mid: #8a1529;
    --crimson-edge: #6d0f1e;
    --charcoal: #333232;
    --charcoal-dark: #2a2929;
    --ink-white: #ffffff;
    --soft-white: #f2f2f2;
  }
  * { box-sizing: border-box; margin: 0; padding: 0; }
  html, body {
    width: 1200px;
    height: 1000px;
    overflow: hidden;
    background: var(--backdrop);
  }
  .canvas {
    position: relative;
    width: 1200px;
    height: 1000px;
  }
  .card {
    position: absolute;
    left: 190px;
    width: 822px;
    height: 470px;
    border-radius: 18px;
    overflow: hidden;
  }
  .card-front {
    top: 23px;
    background: radial-gradient(ellipse at 50% 30%, var(--crimson-core) 0%, var(--crimson-mid) 55%, var(--crimson-edge) 100%);
  }
  .front-pattern {
    position: absolute;
    inset: 0;
    background: radial-gradient(ellipse at 50% 35%, rgba(255,255,255,0) 40%, rgba(0,0,0,0.12) 100%);
  }
  .brand-name {
    position: absolute;
    color: var(--ink-white);
    font-family: "Montserrat", sans-serif;
    font-weight: 500;
    line-height: 1;
    white-space: nowrap;
  }
  .brand-front {
    left: 44px;
    top: 392px;
    font-size: 30px;
    letter-spacing: 1.5px;
  }
  .card-back {
    top: 508px;
    background: linear-gradient(160deg, var(--charcoal) 0%, var(--charcoal-dark) 100%);
  }
  .brand-back {
    left: 38px;
    top: 52px;
    font-size: 28px;
    letter-spacing: 1.5px;
  }
  .person {
    position: absolute;
    left: 38px;
    top: 280px;
    display: flex;
    align-items: baseline;
    gap: 14px;
    color: var(--ink-white);
    white-space: nowrap;
  }
  .person-name {
    font-family: "Montserrat", sans-serif;
    font-weight: 700;
    font-size: 29px;
    letter-spacing: 1px;
  }
  .person-role {
    font-family: "Lato", sans-serif;
    font-size: 20.5px;
    color: var(--soft-white);
    letter-spacing: 0.3px;
    position: relative;
    top: -3px;
  }
  .role-rule {
    position: absolute;
    left: 416px;
    top: 316px;
    width: 40px;
    height: 2px;
    background: var(--soft-white);
  }
  .contact-list {
    position: absolute;
    left: 38px;
    top: 346px;
    list-style: none;
    font-family: "Lato", sans-serif;
    font-size: 20px;
    line-height: 29.5px;
    color: var(--soft-white);
    letter-spacing: 0.3px;
    white-space: nowrap;
  }
  .thanks-lettering {
    position: absolute;
    left: 515px;
    top: 310px;
    width: 272px;
    height: 124px;
    border-radius: 10px;
    background: radial-gradient(ellipse at 45% 50%, rgba(255,255,255,0.16) 0%, rgba(255,255,255,0.05) 60%, rgba(255,255,255,0) 100%);
  }
</style>
</head>
<body>
<div class="canvas">
  <section class="card card-front">
    <div class="front-pattern" role="img" aria-label="Embossed geometric star lattice pattern across the crimson card"></div>
    <span class="brand-name brand-front">742BUILD</span>
  </section>

  <section class="card card-back">
    <span class="brand-name brand-back">742BUILD</span>

    <div class="person">
      <span class="person-name">CLARA VOSS</span>
      <span class="person-role">Managing Director</span>
    </div>
    <span class="role-rule"></span>

    <ul class="contact-list">
      <li>Call: 044-555 018 274</li>
      <li>Email: hello@742build.com</li>
      <li>Webite: 742buildstudio.com</li>
    </ul>

    <div class="thanks-lettering" role="img" aria-label="Hand-lettered 'Thank You' with a small smiley and 'Have Fun!' in white"></div>
  </section>
</div>
</body>
</html>
```